Responsive Website Design for New Social Site (Building User Account)

KelvaPost.com is a website that allows people to create preformatted emails to be sent out at a later date. The purpose is to allow people to communicate in the event of an accident or death. The beta site is built but not consumable by the public. It needs a new look before we go live.

I’m speaking specifically about the user account. They are admin tools for creating and publishing communications. They include workflow design, document/message storage, and a dashboard.

I currently have a basic design. Now I’m looking for an inspired design. Something interesting and memorable. Something that draws people in. I have a PPT that can provide guidance on what elements need to be on each page but I’m looking for someone who knows how to create engaging websites.

SCOPE OF EFFORT
There are approximately 23 pages to the website but only 5 distinct page appearances
• Dashboard
• Workflow
• Document/Message/Contact Management
• Education Search
• Account Form
I need a few pop-up designs
• Yes/No/Continue
I need a responsive design (3 sizes)

ARTISTIC QUALITIES
Easy to Use/Understand
New/Inventive/Cool/Memorable
Works with the Logo
Consistent Elements (buttons, text, use of color, etc)

TECHNICAL ASPECTS
I’d like the work provided in a storyboard and individual files for development

PHASES
1. Initial Concept
a. 2-3 Designs Ideas. Just the Dashboard and Workflow in responsive formats
2. Build
a. Create all the pages
b. Provide in storyboard in responsive formats
c. 2 Rounds of Revision
3. Final
a. Provide Storyboard and Files

I'd like to see a portfolio of your responsive web design, especially any user accounts you have created. I've attached three of the initial pages. I'd like to see a concept of what you would produce for at least one of the pages.

Thank you for your interest.

```html
<!DOCTYPE html>
<html lang="en">
<head>
<meta charset="utf-8">
<title>KelvaPost – Life Plans</title>
<link href="https://fonts.googleapis.com/css2?family=Open+Sans:wght@400;600;700&display=swap" rel="stylesheet">
<style>
:root{
  --page:#f4eaeb;
  --white:#ffffff;
  --blue:#2e9be0;
  --red:#e04343;
  --grey-bar:#8b95a2;
  --side:#7b8898;
  --side-text:#b3bcc7;
  --tab-grey:#d9dbde;
  --ink:#4a4a4a;
  --purple-blue:#6a3fc6;
  --magenta:#a50fb4;
  --green:#079a0a;
  --orange:#e6890b;
  --footer:#434244;
}
*{box-sizing:border-box;margin:0;padding:0}
html,body{width:1014px;height:1200px;overflow:hidden}
body{font-family:"Open Sans",sans-serif;background:var(--page);color:var(--ink);position:relative}
.abs{position:absolute}
.topbar{left:0;top:0;width:1014px;height:81px;background:var(--white)}
.topline{left:0;top:81px;width:1014px;height:3px;background:var(--grey-bar)}
.brand{left:83px;top:28px;display:flex;align-items:center;gap:6px}
.brand-mark{width:20px;height:20px;border-radius:50%;background:var(--blue)}
.brand-name{font-size:15px;font-weight:600;color:var(--blue);line-height:1}
.brand-tag{font-size:4.5px;color:#666;margin-top:2px}
.search{left:325px;top:31px;width:160px;height:23px;background:var(--tab-grey);font-size:9.5px;color:#888;padding:6px 12px}
.search svg{position:absolute;right:10px;top:6px}
.tools{left:858px;top:34px;display:flex;gap:15px}
.sidebar{left:83px;top:84px;width:221px;height:1053px;background:var(--side)}
.avatar{left:108px;top:102px;width:52px;height:52px;border-radius:50%;background:linear-gradient(#d9b79a,#a6785c);border:2px solid #e8e8e8}
.user{left:172px;top:110px;color:var(--white)}
.user .name{font-size:13px;font-weight:600;letter-spacing:1px}
.user .links{font-size:9.5px;margin-top:3px;word-spacing:6px}
.nav{left:83px;top:179px;width:221px}
.nav a{display:flex;align-items:center;height:42px;padding:0 20px 0 24px;color:var(--white);font-size:11.5px;letter-spacing:.5px;text-decoration:none}
.nav a svg.icon{margin-right:10px}
.nav a .chev{margin-left:auto}
.home{background:var(--purple-blue)}.plans{background:var(--magenta)}.docs{background:var(--green)}.contacts{background:var(--orange)}.learning{background:var(--blue)}
.about{left:107px;top:426px;width:180px}
.about h3{color:var(--white);font-size:17px;font-weight:600;letter-spacing:1px;margin-bottom:18px}
.about p{color:var(--side-text);font-size:10px;line-height:18.8px}
.panel-head{left:304px;width:627px;background:var(--blue);color:var(--white);font-size:15.5px;font-weight:600;letter-spacing:1.3px;display:flex;align-items:center;justify-content:center}
.panel-cap{left:304px;width:627px;height:4px;background:var(--grey-bar)}
.tabs{left:304px;top:123px;width:627px;height:38px;background:var(--tab-grey);display:flex}
.tab{height:38px;display:flex;align-items:center;justify-content:center;font-size:11px;color:#555;position:relative}
.tab.active{width:159px;background:var(--red);color:var(--white)}
.tab.active::after{content:"";position:absolute;bottom:-8px;left:72px;border:8px solid transparent;border-top-color:var(--red);border-bottom:0}
.tab.tips{width:141px;border-right:1px solid #c9ccd0}
.meta{left:325px;font-size:11.5px;color:#555}
.meta span{margin-left:8px}
.note{left:304px;top:318px;width:627px;text-align:center;color:var(--red);font-size:11px;line-height:22px}
.card{top:383px;width:186px;height:211px;background:var(--white);text-align:center;padding-top:15px}
.card .ring{display:block;margin:0 auto}
.card h4{font-size:13px;font-weight:600;letter-spacing:1px;color:#444;margin-top:14px}
.card p{font-size:9.8px;line-height:17.5px;color:#555;margin:12px 16px 0}
.tile{top:679px;width:138px;height:80px;color:var(--white);display:flex;flex-direction:column;align-items:center;justify-content:center;font-size:11px;letter-spacing:.5px}
.tile b{font-size:15px;font-weight:700;line-height:1.3}
.tile.orange{background:var(--orange);border-bottom:2px solid #9a5a08}
.tile.green{background:var(--green);border-bottom:2px solid #065e07}
.tile.blue{background:var(--blue);border-bottom:2px solid #1c6fa8}
.tile.purple{background:var(--magenta);border-bottom:2px solid #6e0a7a}
.tile-pointer{left:386px;top:760px;border:9px solid transparent;border-top-color:#9a5a08;border-bottom:0}
.btn{top:783px;height:39px;border:1px solid var(--blue);background:var(--white);color:var(--blue);font-size:18px;font-weight:700;letter-spacing:1.5px;display:flex;align-items:center;justify-content:center}
.selected{left:325px;top:845px;width:607px;height:84px;border:1px solid var(--blue);background:var(--white);padding:16px 9px;display:flex;gap:8px;align-items:flex-start}
.selected .label{color:var(--blue);font-size:11.5px;letter-spacing:.5px;margin:5px 8px 0 0}
.chip{width:87px;height:26px;border:1px solid #e58080;color:var(--red);font-size:10px;display:flex;align-items:center;justify-content:center;position:relative}
.chip svg{position:absolute;right:5px;top:3px}
.group{left:325px;width:606px;font-size:10px;color:#555}
.group h5{font-size:11.5px;font-weight:400;color:#555;margin-bottom:8px}
.group .row{display:flex}
.group .row span:nth-child(1){width:203px}
.group .row span:nth-child(2){width:215px}
.group .row span:nth-child(3){flex:1}
.divider{left:304px;top:1068px;width:627px;height:1px;background:#d0c8ca}
.footer{left:0;top:1137px;width:1014px;height:63px;background:var(--footer);color:#d5d5d5;font-size:10px}
.footer .copy{position:absolute;left:83px;top:24px}
.footer .social{position:absolute;left:755px;top:26px;display:flex;align-items:center;gap:12px;font-size:9.5px}
.footer .dot{width:10px;height:10px;border-radius:50%;background:#bdbdbd}
</style>
</head>
<body>

<header>
  <div class="abs topbar"></div>
  <div class="abs topline"></div>
  <div class="abs brand">
    <div class="brand-mark"></div>
    <div>
      <div class="brand-name">KelvaPost</div>
      <div class="brand-tag">The most trusted resource for life management</div>
    </div>
  </div>
  <div class="abs search">Search
    <svg width="10" height="10" viewBox="0 0 10 10"><circle cx="4.2" cy="4.2" r="3.2" fill="none" stroke="#888" stroke-width="1.2"/><line x1="6.6" y1="6.6" x2="9" y2="9" stroke="#888" stroke-width="1.2"/></svg>
  </div>
  <div class="abs tools">
    <svg width="15" height="15" viewBox="0 0 15 15" fill="#7b8898"><rect y="1" width="15" height="2.5"/><rect y="6.2" width="15" height="2.5"/><rect y="11.4" width="15" height="2.5"/></svg>
    <svg width="15" height="15" viewBox="0 0 15 15" fill="none" stroke="#7b8898" stroke-width="2.2"><path d="M2 9a5 5 0 0 1 9-5"/><path d="M13 6a5 5 0 0 1-9 5"/><path d="M9 2l3 2-2 3" stroke-width="1.8"/></svg>
    <svg width="16" height="16" viewBox="0 0 16 16" fill="#7b8898"><rect width="7" height="7"/><rect x="9" width="7" height="7"/><rect y="9" width="7" height="7"/><rect x="9" y="9" width="7" height="7"/></svg>
  </div>
</header>

<aside>
  <div class="abs sidebar"></div>
  <div class="abs avatar" role="img" aria-label="Member profile photo"></div>
  <div class="abs user">
    <div class="name">DARA QUILL</div>
    <div class="links">View&nbsp;Account Logout</div>
  </div>
  <nav class="abs nav">
    <a class="home"><svg class="icon" width="18" height="16" viewBox="0 0 18 16" fill="#fff"><path d="M9 1 1 8h2.5v7h4v-4h3v4h4V8H17z"/></svg>HOME<svg class="chev" width="6" height="8" viewBox="0 0 6 8"><path d="M1 1l3 3-3 3" stroke="#fff" fill="none" stroke-width="1.3"/></svg></a>
    <a class="plans"><svg class="icon" width="18" height="18" viewBox="0 0 18 18" fill="#fff"><rect x="1" y="6" width="7" height="11"/><rect x="9" y="9" width="7" height="8"/><circle cx="5" cy="4" r="2.5"/><circle cx="12" cy="7" r="2"/></svg>PLANS<svg class="chev" width="6" height="8" viewBox="0 0 6 8"><path d="M1 1l3 3-3 3" stroke="#fff" fill="none" stroke-width="1.3"/></svg></a>
    <a class="docs"><svg class="icon" width="18" height="18" viewBox="0 0 18 18" fill="none" stroke="#fff" stroke-width="1.3"><path d="M3 1h8l4 4v12H3z"/><path d="M6 8h6M6 11h6M6 14h6"/></svg>DOCUMENTS<svg class="chev" width="6" height="8" viewBox="0 0 6 8"><path d="M1 1l3 3-3 3" stroke="#fff" fill="none" stroke-width="1.3"/></svg></a>
    <a class="contacts"><svg class="icon" width="20" height="16" viewBox="0 0 20 16" fill="#fff"><circle cx="10" cy="4" r="3"/><circle cx="4" cy="6" r="2.3"/><circle cx="16" cy="6" r="2.3"/><path d="M4 16c0-5 3-7 6-7s6 2 6 7z"/><path d="M0 15c0-4 2-5 4-5s3 1 3 1L5 15zM20 15c0-4-2-5-4-5s-3 1-3 1l2 4z"/></svg>CONTACTS<svg class="chev" width="6" height="8" viewBox="0 0 6 8"><path d="M1 1l3 3-3 3" stroke="#fff" fill="none" stroke-width="1.3"/></svg></a>
    <a class="learning"><svg class="icon" width="16" height="18" viewBox="0 0 16 18" fill="none" stroke="#fff" stroke-width="1.3"><path d="M8 1a5.5 5.5 0 0 0-3 10v2h6v-2A5.5 5.5 0 0 0 8 1z"/><path d="M5.5 15h5M6.5 17h3"/></svg>LEARNING<svg class="chev" width="6" height="8" viewBox="0 0 6 8"><path d="M1 1l3 3-3 3" stroke="#fff" fill="none" stroke-width="1.3"/></svg></a>
  </nav>
  <section class="abs about">
    <h3>ABOUT US</h3>
    <p>Perspiciatis unde omnis iste natus error sit voluptatem accusantium doloremque laudantium, totam rem aperiam, eaque ipsa quae ab illo inventore veritatis et quasi architecto beatae vitae dicta sunt explicabo. Nemo enim ipsam voluptatem quia voluptas sit aspernatur aut odit aut fugit, sed quia consequuntur magni dolores eos qui ratione voluptatem sequi nesciunt. Neque porro quis­quam est, qui dolorem ipsum quia dolor sit amet, consectetur, adipisci velit, sed quia non numquam eius modi tempora incidunt ut labore et dolore magnam aliquam quaerat voluptatem. Ut enim ad minima veniam, quis nostrum exercitationem ullamaccusantium doloremque lau­dantium, totam rem aperiam, eaque ipsa quae ab illo inventore veritatis et quasi architecto beatae vitae dicta sunt explicabo. Nemo enim ipsam voluptatem quia voluptas sit asper­natur aut odit aut fugit, sed quia consequuntur magni dolores eos qui ratione voluptatem sequi nesciunt. Neque accusantium doloremque laudantium, totam rem aperiam, eaque ipsa quae ab illo inventore veritatis et quasi architecto beatae vitae dicta sunt explicabo. Nemo , quamporro quisquam corporis sus­cipit...</p>
  </section>
</aside>

<main>
  <div class="abs panel-head" style="top:84px;height:39px">LIFE PLANS</div>
  <div class="abs tabs">
    <div class="tab active">BUILD</div>
    <div class="tab tips">TIPS</div>
  </div>
  <div class="abs meta" style="top:189px">Title:<span>LIFE (OR ACCIDENT)</span></div>
  <div class="abs meta" style="top:221px">Date:<span>UNKNOWN</span></div>

  <div class="abs panel-cap" style="top:262px"></div>
  <div class="abs panel-head" style="top:266px;height:39px">VALIDATIONS</div>
  <p class="abs note">Note: LIFE AND ACCIDENT PLANS ARE INITIATED BY YOUR CONTACTS. USE VALIDATIONS TO<br>ENSURE THE EVENT IS PROPERLY REPORTED. CHOOSE ALL THAT APPLY.</p>

  <div class="abs card" style="left:325px">
    <svg class="ring" width="64" height="64" viewBox="0 0 64 64"><circle cx="32" cy="32" r="30.5" fill="none" stroke="#e04343" stroke-width="1.2"/><rect x="24" y="26" width="13" height="13" fill="#e04343"/><path d="M26 31l5 5 10-13" stroke="#fff" stroke-width="4" fill="none"/><path d="M26 31l5 5 10-13" stroke="#e04343" stroke-width="2" fill="none"/></svg>
    <h4>SELF</h4>
    <p>I would you like to validate the events is real before starting the plan. KelvaPost will send me an Approve/Deny request</p>
  </div>
  <div class="abs card" style="left:535px">
    <svg class="ring" width="64" height="64" viewBox="0 0 64 64"><circle cx="32" cy="32" r="30.5" fill="none" stroke="#e04343" stroke-width="1.2"/><rect x="24" y="26" width="13" height="13" fill="#e04343"/><path d="M26 31l5 5 10-13" stroke="#fff" stroke-width="4" fill="none"/><path d="M26 31l5 5 10-13" stroke="#e04343" stroke-width="2" fill="none"/></svg>
    <h4>EXECUTOR</h4>
    <p>I give my executor authority to validate the event and start the plan. KelvaPost will send him/her an Approve/ Deny request</p>
  </div>
  <div class="abs card" style="left:744px">
    <svg class="ring" width="64" height="64" viewBox="0 0 64 64"><circle cx="32" cy="32" r="30.5" fill="none" stroke="#e04343" stroke-width="1.2"/><rect x="24" y="26" width="13" height="13" fill="#e04343"/><path d="M26 31l5 5 10-13" stroke="#fff" stroke-width="4" fill="none"/><path d="M26 31l5 5 10-13" stroke="#e04343" stroke-width="2" fill="none"/></svg>
    <h4>AUTO</h4>
    <p>Automatically start the workflow if no validation is given in X hours from the time the event is reported</p>
  </div>

  <div class="abs panel-cap" style="top:619px"></div>
  <div class="abs panel-head" style="top:623px;height:38px">CREATE EVENT GROUPS</div>
  <div class="abs tile orange" style="left:325px"><b>4</b>CONTACTS</div>
  <div class="abs tile green" style="left:481px"><b>4</b>DOCUMENTS</div>
  <div class="abs tile blue" style="left:637px"><b>1</b>MESSAGES</div>
  <div class="abs tile purple" style="left:793px">FINISH</div>
  <div class="abs tile-pointer"></div>

  <div class="abs btn" style="left:405px;width:255px">CHOOSE EXISTING</div>
  <div class="abs btn" style="left:675px;width:256px">ADD NEW</div>

  <div class="abs selected">
    <span class="label">SELECTED CONTACTS :</span>
    <div class="chip">Angie A<svg width="8" height="8" viewBox="0 0 8 8"><rect x=".5" y=".5" width="7" height="7" fill="none" stroke="#e04343"/><path d="M4 2v4M2 4h4" stroke="#e04343"/></svg></div>
    <div class="chip">Billy B<svg width="8" height="8" viewBox="0 0 8 8"><rect x=".5" y=".5" width="7" height="7" fill="none" stroke="#e04343"/><path d="M4 2v4M2 4h4" stroke="#e04343"/></svg></div>
  </div>

  <div class="abs panel-cap" style="top:955px"></div>
  <div class="abs panel-head" style="top:959px;height:37px">SAVED GROUPS</div>
  <div class="abs group" style="top:1012px">
    <h5>FAMILY</h5>
    <div class="row"><span>Contacts: 4</span><span>Documents: 4</span><span>Messages: 1</span><span>x</span></div>
  </div>
  <div class="abs divider"></div>
  <div class="abs group" style="top:1083px">
    <h5>WORK</h5>
    <div class="row"><span>Contacts: 4</span><span>Documents: 4</span><span>Messages: 1</span><span>x</span></div>
  </div>
</main>

<footer class="abs footer">
  <div class="copy">Copyrights©kelvapost.2015. Allrights Reserved.</div>
  <div class="social">Connect With Us:
    <span class="dot" aria-label="Social link"></span><span class="dot" aria-label="Social link"></span><span class="dot" aria-label="Social link"></span><span class="dot" aria-label="Social link"></span>
  </div>
</footer>

</body>
</html>
```